依頼詳細
【コンテンツ】
基本的なコンテンツは、現在のページ https://korvane.jp/ を元に構成してください。
・[制作実績] ですが、[制作実績 - ホームページ] と [制作実績 - システム開発] に分けて頂き、それぞれ簡単な説明テキスト「○○○…」とイメージ画像などがあると良いかもしれません(ブロック内の正方形のサンプル画像はそのままご使用頂いても [No Photo] 等で代替して頂いても結構です)。
・[お知らせ] と [お問い合わせはこちら] の間に [よくあるご質問] のブロックを追加してください(テキストは「○○○…」で結構です)。
・その他、企業サイトによくあるようなコンテンツで おすすめのコンテンツがございましたら デザイン内にてご提案頂けますと幸いです。

【レイアウト】
・レイアウトは(現状2カラムになってますが)1カラムで構成して頂いても結構です。おすすめのレイアウトでお願いいたします(バナー広告は不要です)。
・幅は1366pxでお願いいたします(最近見かけます画面一杯に広がっているレイアウトはあまり好みではありません。背景画像が画面一杯に広がっているのは構いませんが、コンテンツは中央よりに配置したいと思います。後ほど弊社にてレスポンシブにコーディングする予定です)。
・グローバルメニューは現状の6メニューでお願いいたします。フッターメニューは常時差し替えが発生しますので「○○○」などで代替して頂いて結構です。

【配色・デザイン等】
・配色としては モノトーン(黒)を基調として頂き、見出し背景色などもモノトーンでも結構ですし、あえて一色挙げるとしますと #405080 (HSV 225度 - 50% -50%) などのネイビーまたは青などのクールな色味が好みです。その他のアイキャッチ画像やコンテンツ等の色味は単色でもカラフルなものでも結構です。ブリッカー様のセンスにお任せしたいと思います。
・ロゴマークは先日 Brikka で依頼したものですので、変更せずにそのままご使用ください。
・アイキャッチ等の写真画像は、弊社で Pelmora Images をライセンス契約しておりますので、Pelmora Images のサンプル画像をご使用頂き、別途 画像のURLを当選後にお知らせ頂けましたら結構です。
・アイキャッチ画像のイメージ(内容)ですが、弊社のサービスは 主軸サービス(バックエンド)として (1)システム開発 があり、集客用サービス(フロントエンド)として (2)ホームページ制作 があります。これらのサービスを総合すると (1) を構成する お客様の「笑顔」と弊社の「誠実さ」との「信頼関係」(人間性)がベースとなり、その上に (2) のホームページ制作(デジタルITサービス)が存在する…といったイメージになると思います。それら2つを、例えば半透明にして手前と奥で重ね合わせる/上下にレイアウトする/2枚の画像を JavaScript でアニメーション化するなどは、ブリッカー様のセンスにてお願いできましたらと思います(弊社にてコーディングしますのでご提案ください)。
サイトURL
https://korvane.jp/
ページ数
1ページ
希望イメージ
シンプル 複雑
単色 カラフル
暗い 明るい
日常 高級
遊び心 厳粛
未来的 伝統的
女性的 男性的
希望する色
青系、水色系、グレー系
納品ファイル
• フォトショップ形式 (.psd)
補足説明
Adobe Photoshop CC *psd 形式で、レイヤーを分けて制作・納品頂けますと幸いです。
予想していたよりも提案件数が少なかったので、少し内容をシンプルにして 期間を延長させて頂きました。変更箇所とその他印象等は 以下の通りでございますので、何卒よろしくお願い申し上げます。

【依頼詳細の変更】
・アイキャッチ画像のイメージ(内容)ですが「パソコンで仕事をしている人の笑顔」が含まれている画像でしたらどんなものでも結構です。(すでにご提案頂いているものにつきましては修正して頂かなくても結構です)
・「How to enjoy creative work?」というテキストは入れて頂かない方が良いかと思います(そこまで重要視しておりませんので)。
・見出しテキスト(「制作実績」「お知らせ」など)は左寄せの方が好みです。
・全体の配色ですが、カラフルな感じより 白を基調としたモノトーンな感じの方が好みです。
・[お問い合わせはこちら] ですが、今後 他のページ(ランディングページ)などにも挿入していく可能性がありますので、バナーっぽく制作頂けますと有り難いです。

白を基調としたシンプルなレイアウトで、ディテールまで洗練されていたデザインでしたので 一目見て気に入って選ばせて頂きました。
テンプレートでのデザインが主流になりつつある中、テンプレートでは表現できないような個性のあるものになったのではないかと思いまして 大変満足しております。ありがとうございました。

皆様に個別に御礼メッセージをお送りすることはできませんでしたが、予想以上の大変多くのご提案をご応募頂けまして大変満足しております。本当にありがとうございました。また機会がございましたら 何卒よろしくお願い申し上げます。

```html
<!DOCTYPE html>
<html lang="ja">
<head>
<meta charset="utf-8">
<title>Korvane</title>
<link rel="stylesheet" href="https://fonts.googleapis.com/css2?family=Noto+Sans+JP:wght@400;500;700&family=Roboto:ital,wght@0,400;0,500;0,700;1,700;1,900&display=swap">
<style>
:root{
  --ink:#1a1a1a;
  --text:#333333;
  --muted:#888888;
  --line:#d8d8d8;
  --paper:#ffffff;
  --band:#454545;
  --footer:#3e3e3e;
  --faq-card:#eef5f3;
  --navy:#405080;
}
*{box-sizing:border-box;margin:0;padding:0}
html,body{width:1200px;height:3376px;overflow:hidden}
body{position:relative;background:var(--paper);color:var(--text);font-family:"Noto Sans JP",sans-serif;font-size:13px}
.abs{position:absolute}

/* header */
.site-header{left:0;top:0;width:1200px;height:228px}
.brand{left:148px;top:52px;display:flex;align-items:center;gap:12px}
.brand-mark{width:22px;height:22px;background:var(--ink)}
.brand-name{font-family:"Roboto",sans-serif;font-weight:500;font-size:30px;color:var(--ink);letter-spacing:1px}
.brand-sub{left:148px;top:98px;font-size:10px;color:var(--muted);letter-spacing:2px}
.header-note{right:140px;top:46px;font-size:10px;color:var(--muted)}
.global-nav{right:140px;top:108px;display:flex;gap:4px}
.global-nav a{display:block;padding:8px 14px;font-size:12px;color:var(--text);text-decoration:none;letter-spacing:1px}
.global-nav a.is-current{background:var(--ink);color:#fff}

/* band */
.dark-band{left:0;top:780px;width:1200px;height:1080px;background:var(--band)}

/* hero */
.hero-photo{top:228px;width:452px;height:732px}
.hero-photo.code{left:144px;background:linear-gradient(160deg,#5a6a78,#2c3640 55%,#7a8a96)}
.hero-photo.laptop{left:604px;background:linear-gradient(170deg,#f4f4f4,#dcdcdc 60%,#b8b8b8)}
.hero-copy{left:0;top:470px;width:1200px;text-align:center}
.hero-copy h1{font-family:"Roboto",sans-serif;font-style:italic;font-weight:900;font-size:78px;line-height:86px;color:var(--ink);letter-spacing:4px;-webkit-text-stroke:1px #fff}
.hero-copy p{margin-top:14px;font-size:15px;color:#fff;letter-spacing:2px;text-shadow:0 0 4px rgba(0,0,0,.6)}

/* services */
.service-label{top:960px;width:452px;height:72px;background:var(--ink);color:#fff;text-align:center;padding-top:10px}
.service-label b{display:block;font-family:"Roboto",sans-serif;font-style:italic;font-weight:700;font-size:24px}
.service-label span{font-size:11px;letter-spacing:2px}
.service-desc{top:1064px;width:452px;color:#e6e6e6;font-size:12px;line-height:22px;text-align:center}
.col-l{left:144px}.col-r{left:604px}

.works-grid{top:1148px;width:452px;display:grid;grid-template-columns:repeat(4,1fr);gap:12px 10px}
.work-card{background:#fff;height:254px;padding:8px}
.work-tags{display:flex;gap:4px;margin-bottom:6px}
.work-tags i{font-style:normal;font-size:8px;background:#555;color:#fff;padding:2px 5px}
.work-thumb{height:150px;display:flex;align-items:center;justify-content:center;font-family:"Roboto",sans-serif;font-size:11px;color:var(--muted)}
.work-thumb.nophoto{background:#f1f1f1}
.work-thumb.t1{background:linear-gradient(#e8f0e4,#b7cfa9)}
.work-thumb.t2{background:linear-gradient(#f3f3f3,#cfd7de)}
.work-thumb.t3{background:linear-gradient(#3a3a3a,#7d8a93)}
.work-thumb.t4{background:linear-gradient(#f5f2ea,#d9cfbd)}
.work-thumb.t5{background:linear-gradient(#fff,#e3e9ef)}
.work-thumb.t6{background:linear-gradient(#f2f6e4,#a9c46d)}
.work-thumb.t7{background:linear-gradient(#eef2f6,#b9c6d4)}
.work-cap{margin-top:8px;font-size:9px;line-height:14px;color:var(--text)}
.more-btn{left:480px;top:1706px;width:240px;height:48px;background:#fff;color:var(--ink);font-size:12px;display:flex;align-items:center;justify-content:center;letter-spacing:1px}

/* news */
.section-head{display:flex;align-items:flex-end;gap:10px}
.section-head h2{font-family:"Roboto",sans-serif;font-style:italic;font-weight:700;font-size:34px;letter-spacing:3px}
.section-head small{font-size:10px;padding-bottom:6px;letter-spacing:1px}
.news-head{left:240px;top:1900px;width:720px;color:var(--ink)}
.news-head .rule{flex:1;height:1px;background:var(--ink);margin-bottom:10px}
.news-head .all{font-size:10px;border:1px solid var(--ink);padding:2px 8px;margin-bottom:4px}
.news-list{left:240px;top:1984px;width:720px;list-style:none}
.news-list li{display:flex;gap:40px;height:40px;align-items:center;border-bottom:1px solid var(--line);font-size:12px}
.news-list time{font-family:"Roboto",sans-serif;font-weight:500;width:90px;color:var(--ink)}

/* faq */
.faq-bg{left:0;top:2260px;width:1200px;height:540px;background:linear-gradient(180deg,#2f3437,#4b5459 50%,#2a2e31)}
.faq-head{left:144px;top:2316px;color:#fff}
.faq-grid{left:144px;top:2412px;width:912px;display:grid;grid-template-columns:repeat(3,1fr);gap:20px 24px}
.faq-card{background:var(--faq-card);height:164px;padding:18px 20px;font-size:12px;line-height:20px}
.faq-card p{display:flex;gap:8px}
.faq-card b{font-family:"Roboto",sans-serif;font-weight:700;font-size:15px;color:var(--navy)}
.faq-card .q{color:var(--ink);font-weight:500;border-bottom:1px solid #c9d6d2;padding-bottom:10px;margin-bottom:10px}

/* footer */
.site-footer{left:0;top:2800px;width:1200px;height:576px;background:var(--footer)}
.footer-brand{left:180px;top:2962px;display:flex;align-items:center;gap:12px}
.footer-brand .brand-mark{background:#fff}
.footer-brand .brand-name{color:#fff}
.footer-brand-sub{left:180px;top:3010px;font-size:10px;color:#bbb;letter-spacing:2px}
.contact-banner{left:460px;top:2960px;width:600px;height:120px;border:2px solid #fff;display:flex;flex-direction:column;align-items:center;justify-content:center;color:#fff;outline:1px solid #777;outline-offset:6px}
.contact-banner b{font-family:"Roboto",sans-serif;font-style:italic;font-weight:700;font-size:30px;letter-spacing:4px}
.contact-banner span{font-size:11px;letter-spacing:2px;margin-top:4px}
.footer-nav{left:144px;top:3150px;width:912px;display:flex;justify-content:space-between;font-size:11px;color:#ddd;border-top:1px solid #5a5a5a;border-bottom:1px solid #5a5a5a;padding:16px 10px}
.copyright{left:0;top:3290px;width:1200px;text-align:center;font-family:"Roboto",sans-serif;font-size:10px;color:#999}
</style>
</head>
<body>

<header class="site-header abs">
  <div class="brand abs"><span class="brand-mark"></span><span class="brand-name">Korvane</span></div>
  <div class="brand-sub abs">システム開発・ホームページ制作</div>
  <p class="header-note abs">広島県の企業様向けに、システム開発を行っています</p>
  <nav class="global-nav abs">
    <a class="is-current">トップ</a><a>ホームページ制作</a><a>システム開発</a><a>料金表</a><a>会社概要</a><a>お問い合わせ</a>
  </nav>
</header>

<div class="dark-band abs"></div>

<div class="hero-photo code abs" role="img" aria-label="画面に表示されたプログラムコードのクローズアップ写真"></div>
<div class="hero-photo laptop abs" role="img" aria-label="白い椅子の上に置かれたノートパソコンとスマートフォンの写真"></div>
<div class="hero-copy abs">
  <h1>How to enjoy<br>creative work?</h1>
  <p>お客様の笑顔と誠実さをテーマにしたシステム開発・ホームページ制作</p>
</div>

<div class="service-label col-l abs"><b>System Development</b><span>制作実績 - システム開発</span></div>
<div class="service-label col-r abs"><b>Home Page</b><span>制作実績 - ホームページ</span></div>
<p class="service-desc col-l abs">お客様の業務に合わせた使いやすいシステムを丁寧に開発します。<br>導入後の保守やサポートまで安心してお任せください。</p>
<p class="service-desc col-r abs">集客につながる見やすいホームページを制作します。<br>更新しやすい仕組みで運用までしっかり支えます。</p>

<div class="works-grid col-l abs">
  <article class="work-card"><div class="work-tags"><i>システム</i><i>業務</i></div><div class="work-thumb nophoto">No Photo</div><p class="work-cap">在庫管理システム<br>販売管理の効率化</p></article>
  <article class="work-card"><div class="work-tags"><i>システム</i><i>業務</i></div><div class="work-thumb t1" role="img" aria-label="業務システムの画面"></div><p class="work-cap">顧客管理システム<br>データ一元管理</p></article>
  <article class="work-card"><div class="work-tags"><i>システム</i><i>業務</i></div><div class="work-thumb t2" role="img" aria-label="業務システムの画面"></div><p class="work-cap">予約管理システム<br>受付業務の自動化</p></article>
  <article class="work-card"><div class="work-tags"><i>システム</i><i>業務</i></div><div class="work-thumb t3" role="img" aria-label="業務システムの画面"></div><p class="work-cap">勤怠管理システム<br>集計作業の削減</p></article>
  <article class="work-card"><div class="work-tags"><i>システム</i><i>業務</i></div><div class="work-thumb t2" role="img" aria-label="業務システムの一覧画面"></div><p class="work-cap">受発注システム<br>取引先との連携</p></article>
  <article class="work-card"><div class="work-tags"><i>システム</i><i>業務</i></div><div class="work-thumb nophoto">No Photo</div><p class="work-cap">データ移行ツール<br>バックアップ対応</p></article>
  <article class="work-card"><div class="work-tags"><i>システム</i><i>業務</i></div><div class="work-thumb nophoto">No Photo</div><p class="work-cap">帳票出力システム<br>書類作成の簡略化</p></article>
  <article class="work-card"><div class="work-tags"><i>システム</i><i>業務</i></div><div class="work-thumb nophoto">No Photo</div><p class="work-cap">会員管理システム<br>情報の安全な管理</p></article>
</div>

<div class="works-grid col-r abs">
  <article class="work-card"><div class="work-tags"><i>デザイン</i><i>制作</i></div><div class="work-thumb t4" role="img" aria-label="ホームページのトップ画面"></div><p class="work-cap">美容室サイト<br>予約導線を改善</p></article>
  <article class="work-card"><div class="work-tags"><i>デザイン</i><i>制作</i></div><div class="work-thumb t5" role="img" aria-label="ホームページのトップ画面"></div><p class="work-cap">建設会社サイト<br>施工事例を掲載</p></article>
  <article class="work-card"><div class="work-tags"><i>デザイン</i><i>制作</i></div><div class="work-thumb t1" role="img" aria-label="ホームページのトップ画面"></div><p class="work-cap">飲食店サイト<br>メニュー紹介</p></article>
  <article class="work-card"><div class="work-tags"><i>デザイン</i><i>制作</i></div><div class="work-thumb t7" role="img" aria-label="ホームページのトップ画面"></div><p class="work-cap">士業事務所サイト<br>信頼感を演出</p></article>
  <article class="work-card"><div class="work-tags"><i>デザイン</i><i>制作</i></div><div class="work-thumb t4" role="img" aria-label="ホームページのトップ画面"></div><p class="work-cap">雑貨店サイト<br>商品一覧を整理</p></article>
  <article class="work-card"><div class="work-tags"><i>デザイン</i><i>制作</i></div><div class="work-thumb t6" role="img" aria-label="緑を基調としたホームページの画面"></div><p class="work-cap">教室サイト<br>募集ページ制作</p></article>
  <article class="work-card"><div class="work-tags"><i>デザイン</i><i>制作</i></div><div class="work-thumb t5" role="img" aria-label="ホームページのトップ画面"></div><p class="work-cap">医院サイト<br>診療案内を掲載</p></article>
  <article class="work-card"><div class="work-tags"><i>デザイン</i><i>制作</i></div><div class="work-thumb t7" role="img" aria-label="ホームページのトップ画面"></div><p class="work-cap">工務店サイト<br>施工事例を紹介</p></article>
</div>

<a class="more-btn abs">制作実績一覧はこちら&nbsp;›</a>

<div class="section-head news-head abs"><h2>NEWS</h2><small>お知らせ</small><span class="rule"></span><span class="all">一覧</span></div>
<ul class="news-list abs">
  <li><time>2016.12.28</time>年末年始休業のお知らせ。12月29日から1月4日まで休業いたします。</li>
  <li><time>2016.12.16</time>料金表を更新しました。新しいプランを追加いたしました。</li>
  <li><time>2016.12.01</time>ホームページ制作の新サービスを開始いたしました。</li>
  <li><time>2016.11.15</time>制作実績にシステム開発の事例を追加いたしました。</li>
  <li><time>2016.10.03</time>ホームページをリニューアルいたしました。</li>
</ul>

<div class="faq-bg abs" role="img" aria-label="パソコンで作業するオフィスの風景写真を暗く落とした背景"></div>
<div class="section-head faq-head abs"><h2>FAQ</h2><small>よくあるご質問</small></div>
<div class="faq-grid abs">
  <div class="faq-card"><p class="q"><b>Q.</b>制作期間はどのくらいかかりますか？</p><p><b>A.</b>内容により異なりますが、ホームページは約1〜2ヶ月が目安です。</p></div>
  <div class="faq-card"><p class="q"><b>Q.</b>見積もりは無料で依頼できますか？</p><p><b>A.</b>はい、お見積もりは無料です。お気軽にお問い合わせください。</p></div>
  <div class="faq-card"><p class="q"><b>Q.</b>公開後の更新もお願いできますか？</p><p><b>A.</b>保守プランをご用意しています。更新作業も承ります。</p></div>
  <div class="faq-card"><p class="q"><b>Q.</b>遠方でも依頼することはできますか？</p><p><b>A.</b>メールやオンライン会議で全国から対応が可能です。</p></div>
  <div class="faq-card"><p class="q"><b>Q.</b>既存システムの改修は可能ですか？</p><p><b>A.</b>現状を確認したうえで、最適な改修方法をご提案します。</p></div>
  <div class="faq-card"><p class="q"><b>Q.</b>支払い方法は何がありますか？</p><p><b>A.</b>銀行振込に対応しています。分割もご相談ください。</p></div>
</div>

<footer class="site-footer abs"></footer>
<div class="footer-brand abs"><span class="brand-mark"></span><span class="brand-name">Korvane</span></div>
<div class="footer-brand-sub abs">システム開発・ホームページ制作</div>
<a class="contact-banner abs"><b>CONTACT</b><span>お問い合わせはこちら</span></a>
<nav class="footer-nav abs"><span>ホームページ制作</span><span>システム開発</span><span>料金表</span><span>会社概要</span><span>サイトマップ</span><span>お問い合わせ</span><span>プライバシー</span></nav>
<p class="copyright abs">Copyright © 2016 Korvane All Rights Reserved.</p>

</body>
</html>
```